Website design for Harbourline Bag printing specialist

We need an overhaul of our website front end design. We need a new look and a modern take on the products we sell and service we offer. We sell plain stock in a variety of bag types and offer a printing service of customers branding and logos. Customers request online quotes and this facility must be an easy one step process for users. Our logo is currently green and orange and we are not really looking for re branding at this stage. The final design must communicate that we are the leading printing specialist throughout the country, have been in operation for 15 years and have a vast amount of experience and expertise. The design must instantly show the products available and the ability to request a quote for the desired product.

Target Market(s)

Trade shows, retailers, dentists, food suppliers. wine makers etc etc and anyone that uses carry bags

Industry/Entity Type

Screen Printing

Number of Pages Required

5+ page

Font styles to use
Serif
Sans Serif

Colors

Designer to choose colors to be used in the design.

Requirements
Must have
• Our home page featuring all the products as selectable entities and a short description of what each bag type is when the user hovers over the image.
• Then the product landing pages must show different sizes of that product type. On each page there must be a quick quote button that goes to the quote screen with the features and information to select or include for a quote to be processed. The logo is green and orange and still should have this present but happy to move away from this on the website pages in general.I have so many product pictures and unable to upload them all here. The categories for products are as follows:
• Kraft Paper Bags
• Laminated bags
• Non-woven bags
• Calico bags
• Wine bags
• Florist bags
• Plastic Bags
• Printed Bags
• Gift Boxes
• Tissue paper
• Wrapping Paper
• Custom Bags and Boxes
• There also needs to be a gallery page that showcases work we have done. The ability to have a description for each photo in the gallery would be great.
• A general bag size page would be great and one content page that is about us and another for contact us.
• A free sample button so a user can request a sample. Phone number must be included on this page and unable to submit with a valid phone number.
• Our phone number should be prominent.
• A search feature please.
Nice to have
• Fonts should be in keeping with the design of the website
Should not have
• I dont want users having to scroll too far down to find information. The icons of the bags on the home screen should almost appear on one screen.
• I can upload all my content and pictures so no need to get them from me. I really want your look and feel and design layout that i can then work from.

```html
<!DOCTYPE html>
<html lang="en">
<head>
<meta charset="utf-8">
<title>Harbourline Bags – Home</title>
<link href="https://fonts.googleapis.com/css2?family=Roboto+Condensed:wght@400;700&family=Roboto:ital,wght@0,400;0,500;0,700;1,400&family=Yellowtail&display=swap" rel="stylesheet">
<style>
:root{
  --green:#7dc242;
  --green-dark:#3f8a2a;
  --green-pale:#e9f4e0;
  --orange:#f58220;
  --ink:#1b1b1b;
  --text:#555;
  --grey-band:#ededed;
  --footer:#161616;
  --footer-line:#3a3a3a;
  --white:#fff;
}
*{box-sizing:border-box;margin:0;padding:0}
html,body{width:1200px;height:3422px;overflow:hidden;background:var(--white)}
body{position:relative;font-family:'Roboto',Arial,sans-serif;color:var(--ink)}
.abs{position:absolute}
a{color:inherit;text-decoration:none}

/* top bar */
.topbar{left:0;top:0;width:1200px;height:39px;background:var(--green)}
.topbar .phone{left:855px;top:7px;display:flex;align-items:center;gap:12px;color:var(--white);font-family:'Roboto Condensed',sans-serif;font-weight:700;font-size:21px}
.topbar .phone-dot{width:26px;height:26px;border-radius:50%;background:var(--orange);display:flex;align-items:center;justify-content:center}
.topbar .cart{left:1034px;top:8px;display:flex;align-items:center;gap:10px;color:var(--white);font-size:14px;font-weight:500}

/* header */
.logo{left:75px;top:66px;display:flex;align-items:center;gap:10px;font-family:'Roboto Condensed',sans-serif;font-weight:700;font-size:34px;color:var(--green-dark)}
.logo-mark{width:22px;height:22px;background:var(--orange)}
.nav{left:392px;top:84px;font-size:14.5px;font-weight:400;letter-spacing:.3px}
.nav a{position:absolute;white-space:nowrap;color:#222}
.nav a.current{color:var(--orange)}
.nav a.current::after{content:"";position:absolute;left:0;right:0;bottom:-10px;height:3px;background:var(--orange)}
.search{left:919px;top:73px;width:203px;height:38px;border:1px solid #cfcfcf;display:flex;align-items:center;padding:0 12px;font-size:13px;color:#888;justify-content:space-between}

/* hero */
.hero{left:37px;top:141px;width:1124px;height:541px;overflow:hidden}
.hero-photo{left:0;top:0;width:1124px;height:541px;background:linear-gradient(120deg,#3c3c3c 0%,#777 45%,#4a4a4a 100%)}
.hero-text{left:75px;top:140px;color:var(--white)}
.hero-text .line1{font-family:'Roboto Condensed',sans-serif;font-size:46px;font-weight:700;letter-spacing:1px}
.hero-text .line2{font-family:'Roboto Condensed',sans-serif;font-size:84px;font-weight:700;line-height:.95;letter-spacing:1px}
.hero-text .line3{font-family:'Yellowtail',cursive;font-size:82px;color:var(--orange);line-height:1}
.dots{left:1078px;top:188px;display:flex;flex-direction:column;gap:14px;align-items:center}
.dots span{width:13px;height:13px;border-radius:50%;border:2px solid var(--white)}
.dots span.on{background:var(--orange);border-color:var(--orange)}
.dots .num{border:none;width:auto;height:auto;color:var(--orange);font-size:12px;font-weight:700}

/* features band */
.features{left:37px;top:691px;width:1124px;height:144px;background:var(--grey-band);display:flex}
.feature{flex:1;display:flex;flex-direction:column;align-items:center;justify-content:center;gap:16px;font-family:'Roboto Condensed',sans-serif;font-weight:700;font-size:18px;position:relative}
.feature+.feature::before{content:"";position:absolute;left:0;top:18px;bottom:18px;width:4px;background:#d4d4d4}

/* featured products */
.section-title{width:1200px;left:0;text-align:center;font-family:'Roboto Condensed',sans-serif;font-size:42px;font-weight:400}
.intro{left:250px;width:700px;text-align:center;font-size:13.5px;line-height:29px;color:var(--text)}
.card{top:1047px;width:360px;height:404px;background:var(--green-pale)}
.card .shot{left:90px;top:30px;width:180px;height:160px;border-radius:2px}
.card .badge{left:244px;top:34px;width:44px;height:44px;border-radius:50%;background:var(--orange);display:flex;align-items:center;justify-content:center}
.card h3{left:0;top:232px;width:360px;text-align:center;font-family:'Roboto Condensed',sans-serif;font-size:18px;font-weight:700}
.card .sub{left:0;top:260px;width:360px;text-align:center;font-size:14px;color:#333}
.card .price{left:0;top:290px;width:360px;text-align:center;font-family:'Roboto Condensed',sans-serif;font-size:29px;font-weight:700;color:var(--green)}
.btn{background:var(--orange);color:var(--white);font-family:'Roboto Condensed',sans-serif;font-weight:700;font-size:18px;display:flex;align-items:center;justify-content:center;letter-spacing:.3px}
.card .btn{left:105px;top:331px;width:155px;height:45px}
.divider{left:37px;top:1516px;width:1124px;height:1px;background:#ddd}
.arrow{top:1498px;width:50px;height:38px;border:1px solid #ccc;border-radius:12px;background:var(--white);display:flex;align-items:center;justify-content:center}

/* about */
.about-title{left:121px;top:1615px;font-family:'Roboto Condensed',sans-serif;font-size:42px;font-weight:700}
.about-text{left:123px;width:460px;font-size:13.5px;line-height:27px;color:var(--text)}
.about-shot{left:741px;top:1585px;width:320px;height:417px;background:linear-gradient(135deg,#c9a57c 0%,#e9e6e2 45%,#f28a3a 75%,#f08a8c 100%)}

/* quote band */
.quote-band{left:37px;top:2048px;width:1124px;height:441px;background:var(--green-pale)}
.ring{left:458px;top:2135px;width:370px;height:370px;border-radius:50%;border:24px solid var(--green)}
.model{left:462px;top:2132px;width:280px;height:512px;background:linear-gradient(180deg,#d9cfc8 0%,#e8eaef 35%,#8497b8 65%,#e0317f 100%)}
.quote-text{font-family:'Roboto Condensed',sans-serif;font-weight:700;font-size:18px;line-height:33px;text-transform:uppercase}
.quote-left{left:100px;top:2174px;width:248px;text-align:right}
.quote-right{left:867px;top:2296px;width:280px}
.quote-band-btn{width:214px;height:54px;font-size:20px}

/* newsletter */
.news-title{top:2705px}
.news-sub{left:0;top:2766px;width:1200px;text-align:center;font-style:italic;font-size:15px;color:#444}
.news-input{left:253px;top:2815px;width:536px;height:52px;background:#eee;padding:0 22px;display:flex;align-items:center;font-size:13px;color:#666}
.news-btn{left:789px;top:2815px;width:158px;height:52px}

/* footer */
.footer{left:37px;top:2931px;width:1124px;height:491px;background:radial-gradient(ellipse at 50% 40%,#262626,var(--footer) 70%)}
.footer h4{font-family:'Roboto Condensed',sans-serif;font-weight:700;font-size:18px;color:var(--white)}
.field{left:54px;width:390px;height:40px;border-bottom:1px solid var(--footer-line);color:#aaa;font-size:13px;display:flex;align-items:center;justify-content:space-between;padding:0 6px}
.footer-divider{left:465px;top:60px;width:1px;height:330px;background:var(--footer-line)}
.links{list-style:none;font-size:13.5px;color:#bbb;line-height:30px}
.copy-line{left:0;top:427px;width:1124px;height:1px;background:var(--footer-line)}
.copy{left:0;top:452px;width:1124px;text-align:center;font-size:13px;color:#aaa}
</style>
</head>
<body>

<div class="abs topbar">
  <div class="abs phone">
    <span class="phone-dot">
      <svg width="14" height="14" viewBox="0 0 24 24"><path fill="#fff" d="M6.6 10.8a15.2 15.2 0 0 0 6.6 6.6l2.2-2.2a1 1 0 0 1 1-.25 11.4 11.4 0 0 0 3.6.57 1 1 0 0 1 1 1V20a1 1 0 0 1-1 1A17 17 0 0 1 3 4a1 1 0 0 1 1-1h3.5a1 1 0 0 1 1 1c0 1.25.2 2.45.57 3.57a1 1 0 0 1-.25 1z"/></svg>
    </span>
    123 456 7890
  </div>
  <div class="abs cart">
    <svg width="20" height="22" viewBox="0 0 20 22"><path d="M3 7h14l-1 14H4z" fill="none" stroke="#fff" stroke-width="1.8"/><path d="M7 9V5a3 3 0 0 1 6 0v4" fill="none" stroke="#fff" stroke-width="1.8"/></svg>
    My Cart
  </div>
</div>

<header>
  <div class="abs logo"><span class="logo-mark"></span>Harbourline Bags</div>
  <nav class="abs nav">
    <a class="current" style="left:0">HOME</a>
    <a style="left:78px">PRODUCTS</a>
    <a style="left:192px">GALLERY</a>
    <a style="left:285px">ABOUT US</a>
    <a style="left:393px">CONTACT US</a>
  </nav>
  <div class="abs search">Search...
    <svg width="16" height="16" viewBox="0 0 16 16"><circle cx="6.5" cy="6.5" r="5" fill="none" stroke="#777" stroke-width="1.8"/><path d="M10.5 10.5l4 4" stroke="#777" stroke-width="2"/></svg>
  </div>
</header>

<section class="abs hero">
  <div class="abs hero-photo" role="img" aria-label="Fashion shopper on a city street carrying colourful shopping bags"></div>
  <div class="abs hero-text">
    <div class="line1">CHOOSE YOUR</div>
    <div class="line2">FAVOURITE</div>
    <div class="line3">style</div>
  </div>
  <div class="abs dots">
    <span></span><span></span><span class="on"></span><span class="num">03</span><span style="margin-top:60px"></span><span></span>
  </div>
</section>

<section class="abs features">
  <div class="feature">
    <svg width="52" height="44" viewBox="0 0 52 44" fill="none" stroke="#222" stroke-width="2"><rect x="3" y="8" width="44" height="32" rx="3"/><path d="M8 8l26-6 4 6"/><rect x="34" y="19" width="14" height="10" rx="2"/><circle cx="39" cy="24" r="1.5" fill="#222"/></svg>
    MONEY BACK GUARANTEE
  </div>
  <div class="feature">
    <svg width="56" height="44" viewBox="0 0 56 44" fill="none" stroke="#222" stroke-width="2"><path d="M4 26l10 2 12-14-6-10h5l14 10 10-4c4-1 6 2 2 4L20 40h-5l6-10-9-1-4 4H4z"/></svg>
    FAST SHIPPING
  </div>
  <div class="feature">
    <svg width="52" height="44" viewBox="0 0 52 44" fill="none" stroke="#222" stroke-width="2"><path d="M12 3h28l9 12-23 27L3 15z"/><path d="M3 15h46M18 3l-4 12 12 27 12-27-4-12M14 15h24"/></svg>
    PRODUCT QUALITY
  </div>
  <div class="feature">
    <svg width="48" height="48" viewBox="0 0 48 48" fill="none" stroke="#222" stroke-width="2"><circle cx="24" cy="18" r="9"/><path d="M12 18a12 12 0 0 1 24 0M8 46c1-10 7-15 16-15s15 5 16 15"/><rect x="8" y="16" width="5" height="9" rx="2"/><rect x="35" y="16" width="5" height="9" rx="2"/></svg>
    ONLINE SUPPORT
  </div>
</section>

<section>
  <h2 class="abs section-title" style="top:895px">FEATURED PRODUCTS</h2>
  <p class="abs intro" style="top:954px">Lorem Ipsum is simply dummy text of the printing and typesetting industry. Lorem Ipsum has been the industry's standard dummy text ever since the hen an unknown.</p>

  <article class="abs card" style="left:39px">
    <div class="abs shot" role="img" aria-label="Pink paper wine bag with rope handles" style="background:linear-gradient(150deg,#ff3d97,#d8106a)"></div>
    <div class="abs badge"><svg width="18" height="20" viewBox="0 0 20 22"><path d="M3 7h14l-1 14H4z" fill="none" stroke="#fff" stroke-width="2"/><path d="M7 9V5a3 3 0 0 1 6 0v4" fill="none" stroke="#fff" stroke-width="2"/></svg></div>
    <h3 class="abs">WINE BAGS</h3>
    <p class="abs sub">Lorem ipsum is simple text</p>
    <p class="abs price">$35.00</p>
    <a class="abs btn">VIEW DETAIL</a>
  </article>

  <article class="abs card" style="left:420px">
    <div class="abs shot" role="img" aria-label="Narrow red laminated bottle bag" style="background:linear-gradient(150deg,#c1272d,#7e1216)"></div>
    <div class="abs badge"><svg width="18" height="20" viewBox="0 0 20 22"><path d="M3 7h14l-1 14H4z" fill="none" stroke="#fff" stroke-width="2"/><path d="M7 9V5a3 3 0 0 1 6 0v4" fill="none" stroke="#fff" stroke-width="2"/></svg></div>
    <h3 class="abs">LAMINATED BAGS</h3>
    <p class="abs sub">Lorem ipsum is simple text</p>
    <p class="abs price">$35.00</p>
    <a class="abs btn">VIEW DETAIL</a>
  </article>

  <article class="abs card" style="left:803px">
    <div class="abs shot" role="img" aria-label="Blue non-woven tote bag" style="background:linear-gradient(150deg,#2fb8ec,#1590c8)"></div>
    <div class="abs badge"><svg width="18" height="20" viewBox="0 0 20 22"><path d="M3 7h14l-1 14H4z" fill="none" stroke="#fff" stroke-width="2"/><path d="M7 9V5a3 3 0 0 1 6 0v4" fill="none" stroke="#fff" stroke-width="2"/></svg></div>
    <h3 class="abs">TISSUE PAPER</h3>
    <p class="abs sub">Lorem ipsum is simple text</p>
    <p class="abs price">$35.00</p>
    <a class="abs btn">VIEW DETAIL</a>
  </article>

  <div class="abs divider"></div>
  <a class="abs arrow" style="left:542px"><svg width="12" height="16" viewBox="0 0 12 16"><path d="M9 2L3 8l6 6" fill="none" stroke="#7dc242" stroke-width="2.5"/></svg></a>
  <a class="abs arrow" style="left:606px"><svg width="12" height="16" viewBox="0 0 12 16"><path d="M3 2l6 6-6 6" fill="none" stroke="#7dc242" stroke-width="2.5"/></svg></a>
</section>

<section>
  <h2 class="abs about-title">ABOUT US</h2>
  <p class="abs about-text" style="top:1684px">Lorem Ipsum is simply dummy text of the printing and typesetting industry. Lorem Ipsum has been the industry's Lorem Ipsum is simply dummy text of the printing</p>
  <p class="abs about-text" style="top:1784px">Lorem Ipsum is simply dummy text of the printing and typesetting industry. Lorem Ipsum has been the industry's standard dummy text ever since the 1500s, when an unknown printer took a galley of type and scrambled it to make a type specimen book.</p>
  <a class="abs btn" style="left:123px;top:1907px;width:155px;height:46px">VIEW DETAIL</a>
  <div class="abs about-shot" role="img" aria-label="Group of paper bags in red, kraft, white, orange and pink"></div>
</section>

<section>
  <div class="abs quote-band"></div>
  <div class="abs ring"></div>
  <div class="abs model" role="img" aria-label="Woman seated holding a pink shopping bag"></div>
  <p class="abs quote-text quote-left">We sell plain stock in a variety of bag types</p>
  <a class="abs btn quote-band-btn" style="left:130px;top:2248px">GET ONLINE QUOTE</a>
  <p class="abs quote-text quote-right">Offer a printing service of customers branding and logos</p>
  <a class="abs btn quote-band-btn" style="left:867px;top:2365px">GET ONLINE QUOTE</a>
</section>

<section>
  <h2 class="abs section-title news-title" style="font-weight:700">SIGN UP FOR NEWSLETTER</h2>
  <p class="abs news-sub">Would you like to receive our exclusive news and update for sign up our Newsletter</p>
  <div class="abs news-input">Enter Email *</div>
  <a class="abs btn news-btn">SUBSCRIBE</a>
</section>

<footer class="abs footer">
  <h4 class="abs" style="left:54px;top:62px">GET FREE SAMPLE</h4>
  <div class="abs field" style="top:112px">Name *</div>
  <div class="abs field" style="top:165px">Email *</div>
  <div class="abs field" style="top:217px">Phone *</div>
  <div class="abs field" style="top:270px">Sample Bag *
    <svg width="12" height="8" viewBox="0 0 12 8"><path d="M0 0h12L6 8z" fill="#ccc"/></svg>
  </div>
  <a class="abs btn" style="left:54px;top:329px;width:155px;height:50px">SUBSCRIBE</a>
  <div class="abs footer-divider"></div>

  <h4 class="abs" style="left:522px;top:62px">CONTACT US</h4>
  <ul class="abs links" style="left:524px;top:106px"><li>Home</li><li>Products</li><li>Gallery</li><li>About</li><li>Contact Us</li></ul>

  <h4 class="abs" style="left:723px;top:62px">HELPFULL INFO</h4>
  <ul class="abs links" style="left:725px;top:106px"><li>Help/Faq</li><li>Privacy Policy</li><li>Terms &amp; Conditions</li></ul>

  <h4 class="abs" style="left:932px;top:62px">SHOP WITH US</h4>
  <ul class="abs links" style="left:934px;top:106px"><li>View Cart</li><li>My Account</li><li>Order Traking</li></ul>

  <div class="abs copy-line"></div>
  <p class="abs copy">©Harbourline Bags - 2019 All Rights Reserved.</p>
</footer>

</body>
</html>
```